International Parcel Forwarder needs website redesign and logo

We need an updated website design to make our existing site look more modern, global and trustworthy. Current site
www.parvello.com -- we do not want to rebuild headers or at this point do copyright we are simply looking to make the site pop:)
The service we provide is for shoppers living outside the USA looking to shop here and save money on shipping or get access to stores that won't ship internationally or accept international payment.
Target Market(s)
Online shoppers living outside the USA
Industry/Entity Type
Shipping
Logo Text
US shopping, global shipping
Coding
Coded - Design and coding required
Number of Pages Required
5+ page
Font styles to use

```html
<!DOCTYPE html>
<html lang="en">
<head>
<meta charset="utf-8">
<title>Parvello — US Shopping Global Shipping</title>
<link href="https://fonts.googleapis.com/css2?family=Asap:wght@400;500;600;700&family=Open+Sans:wght@400;600;700&display=swap" rel="stylesheet">
<style>
:root{
  --navy:#0f1d45;
  --navy-deep:#0a1433;
  --blue:#1a4a8e;
  --blue-text:#1b4f96;
  --orange:#f7941d;
  --grey-text:#6b7280;
  --dark-text:#4a4f57;
  --line:#cfe3f0;
  --band:#fdeee0;
  --foot-dark:#1f2a36;
  --white:#ffffff;
  --crimson:#a5141a;
}
*{box-sizing:border-box;margin:0;padding:0}
html,body{width:1200px;height:2250px;overflow:hidden;background:var(--white)}
body{position:relative;font-family:"Open Sans",Arial,sans-serif;color:var(--dark-text)}
.abs{position:absolute}

/* hero */
.hero{left:0;top:0;width:1200px;height:560px}
.hero-bg{position:absolute;inset:0;background:radial-gradient(ellipse at 55% 45%,#1e3478 0%,#12235a 45%,var(--navy-deep) 100%)}
.hero-wave{position:absolute;left:0;top:530px}
.topbar{right:150px;top:12px;display:flex;align-items:center;gap:8px;font-size:12px;color:#c9d1e6;font-weight:600}
.topbar .sep{width:1px;height:14px;background:#7d89a8;margin:0 4px}
.social{width:17px;height:17px;border-radius:50%;background:#b8c0d2}
.brand{display:flex;align-items:center;gap:10px;color:var(--white)}
.brand-dot{width:40px;height:40px;border-radius:50%;background:var(--white)}
.brand-name{font-family:"Asap",Arial,sans-serif;font-weight:600;font-size:20px;letter-spacing:5px;line-height:1}
.brand-tag{font-size:10px;font-weight:600;letter-spacing:.2px;margin-top:3px}
.brand-head{left:145px;top:30px}
.nav{left:499px;top:44px;display:flex;align-items:center;gap:25px;font-size:12px;font-weight:600;color:var(--white)}
.btn{display:inline-flex;align-items:center;justify-content:center;font-weight:700;color:var(--white);text-transform:uppercase;font-size:13px}
.btn-orange{background:var(--orange)}
.btn-blue{background:var(--blue)}
.nav .btn{width:63px;height:28px;text-transform:none;font-size:12px;margin-left:7px}
.hero-title{left:0;width:1200px;top:252px;text-align:center;font-family:"Asap",Arial,sans-serif;font-weight:500;font-size:55px;line-height:56px;color:var(--white);letter-spacing:-.5px}
.hero-cta{left:537px;top:392px;width:127px;height:43px}

/* how it works */
.how-head{left:143px;top:610px;font-family:"Asap",Arial,sans-serif;line-height:1}
.how-head .small{color:var(--orange);font-size:24px;font-weight:500}
.how-head .big{color:var(--blue-text);font-size:40px;margin-top:4px}
.how-head b{font-weight:700}
.step{width:166px;height:166px;border-radius:50%;border:4px solid var(--blue);overflow:hidden}
.step-fill{width:100%;height:100%;background:linear-gradient(180deg,#ffffff 0%,#ffffff 58%,var(--blue) 58%,#12357a 100%)}
.step-num{width:30px;height:30px;border-radius:50%;background:var(--orange);color:var(--white);font-size:13px;font-weight:600;display:flex;align-items:center;justify-content:center;border:2px solid var(--white)}
.rule{left:143px;width:915px;height:1px;background:var(--line)}

/* video + intro */
.video{left:144px;top:1041px;width:444px;height:294px;background:#000}
.video-bar{height:36px;display:flex;align-items:center;justify-content:space-between;padding:0 14px;color:var(--white);font-size:14px}
.video-art{position:absolute;left:0;top:36px;width:444px;height:233px;background:linear-gradient(135deg,#f2c36b 0%,#e8a24a 40%,#3f7cc4 70%,#2aa35b 100%)}
.play{position:absolute;left:198px;top:119px;width:46px;height:32px;border-radius:7px;background:#1c1c1c}
.play::after{content:"";position:absolute;left:18px;top:9px;border-left:13px solid var(--white);border-top:7px solid transparent;border-bottom:7px solid transparent}
.intro-title{left:621px;top:1034px;width:450px;font-family:"Asap",Arial,sans-serif;font-size:33px;line-height:37px;color:var(--blue-text);letter-spacing:-.3px}
.intro-text{left:621px;top:1127px;width:440px;font-size:14.5px;line-height:22.5px;color:var(--grey-text)}
.intro-btn1{left:621px;top:1275px;width:127px;height:43px}
.intro-btn2{left:756px;top:1275px;width:128px;height:43px}

/* why */
.why-title{left:0;width:1200px;top:1444px;text-align:center;font-family:"Asap",Arial,sans-serif;font-size:41px;font-weight:500;letter-spacing:-.5px}
.why-title .o{color:var(--orange)}
.why-title .b{color:var(--blue-text);font-weight:700}
.feat-icon{width:132px;height:132px;border-radius:50%;border:2px solid var(--orange);display:flex;align-items:center;justify-content:center}
.feat-title{font-family:"Asap",Arial,sans-serif;font-weight:700;font-size:24px;color:#555a62;letter-spacing:.2px}
.feat-list{list-style:none;margin-top:8px}
.feat-list li{position:relative;padding-left:24px;font-size:14.5px;line-height:18px;color:var(--grey-text);margin-bottom:9px;letter-spacing:-.2px}
.feat-list li::before{content:"";position:absolute;left:2px;top:2px;width:6px;height:11px;border-right:3px solid var(--blue);border-bottom:3px solid var(--blue);transform:rotate(40deg)}

/* stores */
.stores{left:0;top:1942px;width:1200px;height:128px;background:var(--band);display:flex;align-items:center;justify-content:space-between;padding:0 145px}
.store{font-family:"Asap",Arial,sans-serif;font-size:30px;font-weight:600;color:#8e8e8e}

/* footer */
.footer{left:0;top:2070px;width:1200px;height:98px;background:var(--blue)}
.brand-foot{left:145px;top:2094px}
.foot-nav{left:624px;top:2111px;display:flex;gap:18px;font-size:12px;font-weight:600;color:var(--white)}
.partners{left:0;top:2168px;width:1200px;height:82px;background:var(--foot-dark);text-align:center}
.partners-label{padding-top:22px;font-size:11px;letter-spacing:1px;color:#5d6875;font-weight:600}
.partners-list{display:flex;justify-content:center;gap:26px;margin-top:9px;font-family:"Asap",Arial,sans-serif;font-size:15px;font-weight:700;color:#6d7886}
</style>
</head>
<body>

<section class="abs hero">
  <div class="hero-bg" role="img" aria-label="Dark blue world map with glowing shipping routes connecting continents"></div>
  <svg class="hero-wave" width="1200" height="30" viewBox="0 0 1200 30" aria-hidden="true">
    <path d="M0 16 Q10 6 20 16 T40 16 T60 16 T80 16 T100 16 T120 16 T140 16 T160 16 T180 16 T200 16 T220 16 T240 16 T260 16 T280 16 T300 16 T320 16 T340 16 T360 16 T380 16 T400 16 T420 16 T440 16 T460 16 T480 16 T500 16 T520 16 T540 16 T560 16 T580 16 T600 16 T620 16 T640 16 T660 16 T680 16 T700 16 T720 16 T740 16 T760 16 T780 16 T800 16 T820 16 T840 16 T860 16 T880 16 T900 16 T920 16 T940 16 T960 16 T980 16 T1000 16 T1020 16 T1040 16 T1060 16 T1080 16 T1100 16 T1120 16 T1140 16 T1160 16 T1180 16 T1200 16 L1200 30 L0 30 Z" fill="#ffffff"/>
  </svg>

  <div class="abs topbar">
    <span>1-555-014-2290</span><span class="sep"></span>
    <span class="social"></span><span class="social"></span><span class="social"></span>
  </div>

  <div class="abs brand brand-head">
    <span class="brand-dot"></span>
    <div><div class="brand-name">PARVELLO</div><div class="brand-tag">US Shopping Global Shipping</div></div>
  </div>

  <nav class="abs nav">
    <span>Shipping Calculator</span><span>How It Works</span><span>Parvello Pricing</span><span>Blog</span><span>Contact Us</span>
    <span class="btn btn-orange">Login</span>
  </nav>

  <h1 class="abs hero-title">Shop at any U.S. retailer.<br>Ship anywhere.</h1>
  <span class="abs btn btn-orange hero-cta">Learn More</span>
</section>

<section>
  <div class="abs how-head">
    <div class="small">How</div>
    <div class="big"><b>Parvello</b> works</div>
  </div>

  <div class="abs step" style="left:146px;top:723px"><div class="step-fill" role="img" aria-label="Step 1: Statue of Liberty with location pin"></div></div>
  <div class="abs step" style="left:394px;top:723px"><div class="step-fill" role="img" aria-label="Step 2: Shop storefront"></div></div>
  <div class="abs step" style="left:642px;top:723px"><div class="step-fill" role="img" aria-label="Step 3: Notification bell"></div></div>
  <div class="abs step" style="left:890px;top:723px"><div class="step-fill" role="img" aria-label="Step 4: Cargo ship"></div></div>

  <div class="abs step-num" style="left:143px;top:742px">01</div>
  <div class="abs step-num" style="left:391px;top:742px">02</div>
  <div class="abs step-num" style="left:639px;top:742px">03</div>
  <div class="abs step-num" style="left:887px;top:742px">04</div>

  <svg class="abs" style="left:312px;top:790px" width="90" height="40" aria-hidden="true"><path d="M4 22 Q40 34 76 18" fill="none" stroke="#d6d8dc" stroke-width="4"/><path d="M70 10 L84 16 L72 26 Z" fill="#d6d8dc"/></svg>
  <svg class="abs" style="left:560px;top:784px" width="90" height="40" aria-hidden="true"><path d="M4 30 Q40 10 76 14" fill="none" stroke="#d6d8dc" stroke-width="4"/><path d="M70 6 L84 14 L71 22 Z" fill="#d6d8dc"/></svg>
  <svg class="abs" style="left:808px;top:790px" width="90" height="40" aria-hidden="true"><path d="M4 16 Q40 34 76 24" fill="none" stroke="#d6d8dc" stroke-width="4"/><path d="M69 16 L84 22 L71 31 Z" fill="#d6d8dc"/></svg>

  <div class="abs rule" style="top:960px"></div>

  <div class="abs video">
    <div class="video-bar"><span>How Parvello Works</span>
      <svg width="16" height="14" viewBox="0 0 16 14" aria-hidden="true"><path d="M9 1 L15 6 L9 11 V8 C5 8 3 9 1 13 C1 7 4 4 9 4 Z" fill="#fff"/></svg>
    </div>
    <div class="video-art" role="img" aria-label="Cartoon of a couple at a desk with a laptop showing the shipping website"></div>
    <span class="play"></span>
  </div>

  <h2 class="abs intro-title" style="font-weight:400">Lorem ipsum dolor sit amet, consectetur adipiscing elit, sed.</h2>
  <p class="abs intro-text">Lorem ipsum dolor sit amet, consectetur adipiscing elit, sed do eiusmod tempor incididunt ut labore et dolore magna aliqua. Utos enim ad minim veniam, quis nostrud exercitation ullamco aman laborislaborum elit. Lorem ipsum dolor sit amet, consectetur adipiscing elit, sed do eiusmod tempor incididunt.</p>
  <span class="abs btn btn-orange intro-btn1">Learn More</span>
  <span class="abs btn btn-blue intro-btn2">Sign Up Today</span>

  <div class="abs rule" style="top:1398px"></div>
</section>

<section>
  <h2 class="abs why-title"><span class="o">Why Use </span><span class="b">Parvello</span></h2>

  <div class="abs feat-icon" style="left:144px;top:1535px">
    <svg width="70" height="50" viewBox="0 0 70 50" fill="none" stroke="#666" stroke-width="2" aria-hidden="true">
      <rect x="4" y="14" width="38" height="24"/><path d="M42 22 H56 L64 31 V38 H42 Z"/><circle cx="16" cy="41" r="5" fill="#fff"/><circle cx="54" cy="41" r="5" fill="#fff"/><circle cx="14" cy="10" r="8" fill="#fff"/><path d="M10 10 L13 13 L18 7"/>
    </svg>
  </div>
  <div class="abs" style="left:298px;top:1537px">
    <div class="feat-title">EXPERIENCE</div>
    <ul class="feat-list"><li>30 years experience<br>in international shipping.</li><li>Excellent customer service</li></ul>
  </div>

  <div class="abs feat-icon" style="left:611px;top:1535px">
    <svg width="50" height="60" viewBox="0 0 50 60" fill="none" stroke="#666" stroke-width="2" aria-hidden="true">
      <path d="M18 14 L14 4 H36 L32 14"/><path d="M18 14 C6 24 2 36 6 48 C10 56 40 56 44 48 C48 36 44 24 32 14 Z"/><circle cx="25" cy="36" r="11"/><text x="25" y="41" font-size="14" text-anchor="middle" fill="#666" stroke="none" font-family="Arial,sans-serif">$</text>
    </svg>
  </div>
  <div class="abs" style="left:765px;top:1537px">
    <div class="feat-title">VALUE</div>
    <ul class="feat-list"><li>Discounted shipping rates with<br>major carriers</li><li>No membership or joining fees</li><li>Low consolidation fees</li></ul>
  </div>

  <div class="abs feat-icon" style="left:144px;top:1720px">
    <svg width="76" height="40" viewBox="0 0 76 40" fill="none" stroke="#666" stroke-width="2" aria-hidden="true">
      <rect x="2" y="10" width="10" height="20"/><rect x="64" y="10" width="10" height="20"/><path d="M12 14 H28 L38 20 L30 24 L24 20 M12 26 H22 L34 34 L52 24 L64 26 M64 14 H48 L38 20"/>
    </svg>
  </div>
  <div class="abs" style="left:298px;top:1722px">
    <div class="feat-title">TRUST</div>
    <ul class="feat-list"><li>Excellent customer service</li><li>A+ rating from the Consumer<br>Trust Council</li></ul>
  </div>

  <div class="abs feat-icon" style="left:611px;top:1720px">
    <svg width="66" height="56" viewBox="0 0 66 56" fill="none" stroke="#666" stroke-width="2" aria-hidden="true">
      <circle cx="34" cy="10" r="7"/><ellipse cx="32" cy="32" rx="22" ry="15"/><path d="M18 44 V52 M44 44 V52 M54 30 H62"/><circle cx="44" cy="28" r="1.5" fill="#666"/>
    </svg>
  </div>
  <div class="abs" style="left:765px;top:1722px">
    <div class="feat-title">SAVINGS</div>
    <ul class="feat-list"><li>No fees to receive packages</li><li>No U.S. sales tax when using our<br>New Hampshire warehouse</li><li>Low consolidation fees</li></ul>
  </div>
</section>

<section class="abs stores">
  <span class="store">Tillery</span>
  <span class="store">Orbazon</span>
  <span class="store">Everly 9</span>
  <span class="store">Copper Dusk</span>
  <span class="store">Halstead</span>
  <span class="store">Brightway</span>
</section>

<footer>
  <div class="abs footer"></div>
  <div class="abs brand brand-foot">
    <span class="brand-dot"></span>
    <div><div class="brand-name">PARVELLO</div><div class="brand-tag">US Shopping Global Shipping</div></div>
  </div>
  <nav class="abs foot-nav"><span>How it Works</span><span>Pricing</span><span>Terms of Service</span><span>Privacy Policy</span><span>Contact Us</span></nav>
  <div class="abs partners">
    <div class="partners-label">IN PARTNERSHIP WITH</div>
    <div class="partners-list"><span>Swiftline</span><span>Postal Direct</span><span>Kestrel Air</span></div>
  </div>
</footer>

</body>
</html>
```